LumaForm Informational Flyer Design

Hello, we are a team of two who opened an all women's gym located in Seattle, WA. We've been in business for four and a half years renting from various other facilities such as crossfit, a banquet hall, and outside at local parks, and opened our own facility in January 2016.
Check www.lumaformstudio.example for more info about our gym, our team, and what we offer to our clients.
We are looking for a strong, clean, but feminine double-sided leaflet or something a little larger than the average postcard to pass out to local businesses, schools and other charitable auctions, and neighboring apartment buildings that are currently under construction. DL size
We have more images should you need them for the design, some more abstract of just equipment; included a few here along with our logo.
Please let me know if you need more info or more pics.
Thanks in advance!

Hello, I have updated the brief with more specifics. Please take a look and resubmit with thanks. Added Thursday, February 16, 2017

Target Market(s)

Women ages 18-70

Industry/Entity Type

Fitness

Font styles to use
Other font styles liked:
• Futura (SEE NOTES)

Colors
e34197
000000

Requirements
Must have
• DL Size
• Front should be clean and simple and include:
• • LOGO
• • RESULTS-DRIVEN WOMEN’S FITNESS
• • FREE INTRODUCTORY WEEK
• • pictures of LUMASPRINT, LUMAPOISE, & LUMASTILL with names overlaid on pictures (see home page of website)
• ◦ *CHILDCARE INCLUDED (underneath program pictures, but not too big)
• BACK side:
• • LumaForm is not just a women's gym. We are a community of women grinding and growing into the very best versions of ourselves.  LumaForm’s mission is simple -- to get you strong, balanced, and flexible for life both in and out of the gym.
• • PROGRAMS:   (Optional to include pictures of each program)
• LUMASPRINT underneath should list ASCEND & LUMABEGIN
• LUMAPOISE
• LUMASTILL underneath should list LUMA TIDE MOTION & RESTORATIVE YOGA
• • PRICING (includes childcare)
• ANNUAL $1675
• MONTHLY $159
• 10 CLASS PASS $199
• DROP-IN $25
• *See website for special discounts*
• • Phone
• • Email
• • Address
• • Website
• • COUPON CODE section with some space underneath to handwrite in a coupon code. 
Nice to have
• If it works with the design and doesn't make it too cluttered, instead of FREE INTRODUCTORY WEEK on front side, can say CLAIM YOUR FREE INTRO WEEK HERE (or some other wording) and include a QR code that goes directly to our scheduling site: https://lumaform.bookingdesk.example/hello
• Can use the fonts in the logo or designer preference on what will work best with design.

```html
<!DOCTYPE html>
<html lang="en">
<head>
<meta charset="utf-8">
<title>LumaForm Flyer – Back Side</title>
<link rel="stylesheet" href="https://fonts.googleapis.com/css2?family=Jost:wght@600;700;800&display=swap">
<style>
  :root {
    --pink: #e34197;
    --pink-deep: #c23a9e;
    --pink-light: #e86fb0;
    --charcoal: #2e2e30;
    --charcoal-soft: #4a4648;
    --white: #ffffff;
  }
  html, body {
    margin: 0;
    padding: 0;
    width: 1200px;
    height: 2546px;
    overflow: hidden;
    background: var(--white);
  }
  .flyer {
    position: relative;
    width: 1200px;
    height: 2546px;
    overflow: hidden;
    font-family: "Jost", "Futura", sans-serif;
    font-weight: 700;
    color: var(--white);
    text-transform: none;
  }
  .photo-backdrop {
    position: absolute;
    inset: 0;
    background:
      linear-gradient(90deg, transparent 0 50%, var(--charcoal) 50% 100%),
      linear-gradient(180deg, var(--pink-light) 0%, var(--pink) 45%, var(--pink-deep) 100%);
  }
  .photo-backdrop::after {
    content: "";
    position: absolute;
    left: 600px; right: 0; top: 0; bottom: 0;
    background: radial-gradient(ellipse at 70% 35%, var(--charcoal-soft) 0%, var(--charcoal) 70%);
  }
  .line {
    position: absolute;
    margin: 0;
    line-height: 1;
    white-space: nowrap;
  }
  .centered { left: 0; width: 1200px; text-align: center; }
  .underlined {
    text-decoration: underline;
    text-decoration-thickness: 6px;
    text-underline-offset: 12px;
  }
  .side-label {
    position: absolute;
    left: 50px;
    top: 883px;
    transform: translate(-50%, -50%) rotate(-90deg);
    font-size: 56px;
    letter-spacing: 4px;
    line-height: 1;
    white-space: nowrap;
  }
  .intro {
    position: absolute;
    left: 192px;
    top: 12px;
    width: 840px;
    margin: 0;
    font-size: 33px;
    line-height: 39px;
    text-transform: uppercase;
  }
  .section-title { font-size: 146px; font-weight: 800; letter-spacing: 3px; }
  .program { font-size: 68px; }
  .program-large { font-size: 78px; }
  .sub-program { font-size: 52px; }
  .pricing-item { left: 196px; font-size: 72px; letter-spacing: 1px; }
  .contact-title { font-size: 52px; text-decoration-thickness: 4px; text-underline-offset: 8px; }
  .phone { font-size: 110px; letter-spacing: 2px; }
  .contact-detail { font-size: 52px; }
  .coupon-title { font-size: 64px; }
  .coupon-box {
    position: absolute;
    left: 188px;
    top: 2316px;
    width: 825px;
    height: 196px;
    background: var(--white);
  }
</style>
</head>
<body>
<main class="flyer">
  <div class="photo-backdrop" role="img" aria-label="Photo of a woman training in the gym, tinted pink on the left half and dark grey on the right"></div>

  <div class="side-label">BACK SIDE</div>

  <p class="intro">LumaForm is not just a women’s gym. We are a community of women grinding and growing into the very best versions of ourselves.<br>LumaForm’s mission is simple-to get you strong and balanced, and flexible for life both in and out of the gym.</p>

  <h2 class="line centered section-title underlined" style="top:478px">PROGRAMS:</h2>

  <p class="line centered program underlined" style="top:700px">LUMASPRINT:</p>
  <p class="line centered sub-program" style="top:776px">ASCEND</p>
  <p class="line centered sub-program" style="top:857px">LUMABEGIN</p>
  <p class="line centered program underlined" style="top:904px">LUMAPOISE</p>
  <p class="line centered program-large underlined" style="top:1000px">LUMASTILL:</p>
  <p class="line centered sub-program" style="top:1125px">LUMA TIDE MOTION</p>
  <p class="line centered sub-program" style="top:1209px">RESTORATIVE YOGA</p>

  <h2 class="line centered section-title underlined" style="top:1300px">PRICING:</h2>

  <p class="line pricing-item" style="top:1460px">-ANNUAL $1675</p>
  <p class="line pricing-item" style="top:1561px">-MONTHLY $159</p>
  <p class="line pricing-item" style="top:1642px">-10 CLASS PASS $199</p>
  <p class="line pricing-item" style="top:1738px">-DROP-IN $25</p>

  <p class="line centered contact-title underlined" style="top:1820px">CONTACT US &amp; FIND US:</p>
  <p class="line centered phone" style="top:1888px">206-555-0148</p>
  <p class="line centered contact-detail" style="top:2009px">1200 Linden Ridge Ave SW</p>
  <p class="line centered contact-detail" style="top:2094px">Seattle, WA 98116</p>
  <p class="line centered contact-detail" style="top:2166px">hello@lumaformstudio.example</p>
  <p class="line centered coupon-title" style="top:2231px">COUPON CODE:</p>

  <div class="coupon-box" aria-label="Space to write a coupon code"></div>
</main>
</body>
</html>
```